Türschildvorlagen mit Alternativfarben für ein Pflegeheim (Bewohnerzimmer & andere Räume)
Zielgruppe
Der Birkenau ist ein privates Alten- und Pflegeheim. Im Zuge von Umbaumaßnahmen sollen die Türschilder im Haus neu gestsltet werden. Die Türschilder hängen in einer Kunststoff-Halterung neben jeder Tür (Bewohnerzimmer, Funktionsräume etc.). (Siehe zur Veranschaulichung die angehängte Datei 'Beispielfoto Türschild.jpg). Die Gebäudeebenen sind farblich unterschiedlich gestaltet, was auch in den Türschildern aufgegriffen werden soll (siehe Aufgabenstellung).
Aufgabenstellung
Für die Türschildhalterungen soll eine optisch ansprechende Türschildvorlage erstellt werden. Die Vorlage muss folgende Kriterien erfüllen:
1. Exakte Maße der Vorlage: Breite: 14,8 cm, Höhe: 10,8 cm.
2. Inhalte:
a) Zimmernummer (3 oder 4-stellig)
b) Name des Bewohners / des Raumes
c) Grafikelement, das das Firmenlogo aufgreift (Nachträglicher Hinweis: Das Logo muss nicht 1 zu 1 übernommen werden sondern kann variiert werden als Designelement. Auch der BIRKENAU-Schriftzug kann entfallen!)
d) Farbcode für die jeweilige Gebäudeebene
==> Farben der Ebenen:
E0: Lichtgrün (RAL 6027, CMYK 60 0 30 0); E1: Narzissengelb (RAL 1007, CMYK 0 40 100 0); E2: Signalblau (RAL 5005, CMYK 100 40 0 40); E3: Verkehrsrot (RAL 3020, CMYK 0 100 100 10); E4: Wasserblau (RAL 5021, CMYK 100 20 50 10); E5: Signalorange (RAL 2010, CMYK 0 70 100 10); E6: Patinagrün (RAL 6000, CMYK 80 20 60 20)
3. Die Vorlage sollte möglichst einfach mit "handelsüblichen Programmen" (MS Word?) editiert werden können (Ändern Zimmernummer + Name).

```html
<!DOCTYPE html>
<html lang="de">
<head>
<meta charset="utf-8">
<title>Türschilder Birkenau – Ebenen E0 bis E6</title>
<link href="https://fonts.googleapis.com/css2?family=Open+Sans:wght@400;700&display=swap" rel="stylesheet">
<style>
  :root {
    --ink: #183c78;
    --brand: #1f4f9e;
    --paper: #ffffff;
    --sheet: #ffffff;
    --level-e0: #66c0bb;
    --level-e1: #f4a608;
    --level-e2: #004f82;
    --level-e3: #d0121a;
    --level-e4: #007d7e;
    --level-e5: #db6010;
    --level-e6: #1f8066;
  }
  html, body {
    margin: 0;
    padding: 0;
    width: 801px;
    height: 1200px;
    overflow: hidden;
    background: var(--sheet);
  }
  .sign-sheet {
    position: relative;
    width: 801px;
    height: 1200px;
  }
  .door-sign {
    position: absolute;
    width: 378px;
    height: 276px;
    display: block;
    box-shadow: 5px 5px 6px rgba(0,0,0,0.45);
    background: var(--paper);
  }
  .col-left  { left: 7px; }
  .col-right { left: 404px; }
  .row-1 { top: 7px; }
  .row-2 { top: 304px; }
  .row-3 { top: 600px; }
  .row-4 { top: 897px; }

  .e0 { --level: var(--level-e0); }
  .e1 { --level: var(--level-e1); }
  .e2 { --level: var(--level-e2); }
  .e3 { --level: var(--level-e3); }
  .e4 { --level: var(--level-e4); }
  .e5 { --level: var(--level-e5); }
  .e6 { --level: var(--level-e6); }

  .level-field { fill: var(--level); }
  .field-edge { fill: var(--ink); }
  .swoosh { fill: var(--ink); }
  .level-code {
    font-family: "Open Sans", Arial, sans-serif;
    font-weight: 400;
    font-size: 58px;
    fill: var(--ink);
  }
  .room-number {
    font-family: "Open Sans", Arial, sans-serif;
    font-weight: 700;
    font-size: 28px;
    fill: var(--ink);
  }
  .room-name {
    font-family: "Open Sans", Arial, sans-serif;
    font-weight: 700;
    font-size: 37px;
    fill: #ffffff;
  }
  .home-name {
    font-family: "Open Sans", Arial, sans-serif;
    font-weight: 700;
    font-size: 25px;
    fill: var(--brand);
  }
</style>
</head>
<body>
<main class="sign-sheet">

  <svg class="door-sign e0 col-left row-1" viewBox="0 0 420 307" aria-label="Türschild Ebene E0">
    <path class="level-field" d="M155,0 C150,120 195,235 285,307 L420,307 L420,0 Z"/>
    <path class="field-edge" d="M146,0 L157,0 C152,110 190,225 285,307 C205,240 150,130 146,0 Z"/>
    <path class="swoosh" d="M0,146 Q85,122 168,124 L172,133 Q90,128 0,160 Z"/>
    <text class="level-code" x="36" y="78">E0</text>
    <text class="room-number" x="38" y="110">1230</text>
    <text class="room-name" x="418" y="172" text-anchor="end">WC-Damen</text>
    <text class="home-name" x="34" y="272">BIRKENAU</text>
  </svg>

  <svg class="door-sign e1 col-right row-1" viewBox="0 0 420 307" aria-label="Türschild Ebene E1">
    <path class="level-field" d="M155,0 C150,120 195,235 285,307 L420,307 L420,0 Z"/>
    <path class="field-edge" d="M146,0 L157,0 C152,110 190,225 285,307 C205,240 150,130 146,0 Z"/>
    <path class="swoosh" d="M0,146 Q85,122 168,124 L172,133 Q90,128 0,160 Z"/>
    <text class="level-code" x="36" y="78">E1</text>
    <text class="room-number" x="38" y="110">1230</text>
    <text class="room-name" x="418" y="172" text-anchor="end">WC-Damen</text>
    <text class="home-name" x="34" y="272">BIRKENAU</text>
  </svg>

  <svg class="door-sign e2 col-left row-2" viewBox="0 0 420 307" aria-label="Türschild Ebene E2">
    <path class="level-field" d="M155,0 C150,120 195,235 285,307 L420,307 L420,0 Z"/>
    <path class="field-edge" d="M146,0 L157,0 C152,110 190,225 285,307 C205,240 150,130 146,0 Z"/>
    <path class="swoosh" d="M0,146 Q85,122 168,124 L172,133 Q90,128 0,160 Z"/>
    <text class="level-code" x="36" y="78">E2</text>
    <text class="room-number" x="38" y="110">1230</text>
    <text class="room-name" x="418" y="172" text-anchor="end">WC-Damen</text>
    <text class="home-name" x="34" y="272">BIRKENAU</text>
  </svg>

  <svg class="door-sign e3 col-right row-2" viewBox="0 0 420 307" aria-label="Türschild Ebene E3">
    <path class="level-field" d="M155,0 C150,120 195,235 285,307 L420,307 L420,0 Z"/>
    <path class="field-edge" d="M146,0 L157,0 C152,110 190,225 285,307 C205,240 150,130 146,0 Z"/>
    <path class="swoosh" d="M0,146 Q85,122 168,124 L172,133 Q90,128 0,160 Z"/>
    <text class="level-code" x="36" y="78">E3</text>
    <text class="room-number" x="38" y="110">1230</text>
    <text class="room-name" x="418" y="172" text-anchor="end">WC-Damen</text>
    <text class="home-name" x="34" y="272">BIRKENAU</text>
  </svg>

  <svg class="door-sign e4 col-left row-3" viewBox="0 0 420 307" aria-label="Türschild Ebene E4">
    <path class="level-field" d="M155,0 C150,120 195,235 285,307 L420,307 L420,0 Z"/>
    <path class="field-edge" d="M146,0 L157,0 C152,110 190,225 285,307 C205,240 150,130 146,0 Z"/>
    <path class="swoosh" d="M0,146 Q85,122 168,124 L172,133 Q90,128 0,160 Z"/>
    <text class="level-code" x="36" y="78">E4</text>
    <text class="room-number" x="38" y="110">1230</text>
    <text class="room-name" x="418" y="172" text-anchor="end">WC-Damen</text>
    <text class="home-name" x="34" y="272">BIRKENAU</text>
  </svg>

  <svg class="door-sign e5 col-right row-3" viewBox="0 0 420 307" aria-label="Türschild Ebene E5">
    <path class="level-field" d="M155,0 C150,120 195,235 285,307 L420,307 L420,0 Z"/>
    <path class="field-edge" d="M146,0 L157,0 C152,110 190,225 285,307 C205,240 150,130 146,0 Z"/>
    <path class="swoosh" d="M0,146 Q85,122 168,124 L172,133 Q90,128 0,160 Z"/>
    <text class="level-code" x="36" y="78">E5</text>
    <text class="room-number" x="38" y="110">1230</text>
    <text class="room-name" x="418" y="172" text-anchor="end">WC-Damen</text>
    <text class="home-name" x="34" y="272">BIRKENAU</text>
  </svg>

  <svg class="door-sign e6 col-left row-4" viewBox="0 0 420 307" aria-label="Türschild Ebene E6">
    <path class="level-field" d="M155,0 C150,120 195,235 285,307 L420,307 L420,0 Z"/>
    <path class="field-edge" d="M146,0 L157,0 C152,110 190,225 285,307 C205,240 150,130 146,0 Z"/>
    <path class="swoosh" d="M0,146 Q85,122 168,124 L172,133 Q90,128 0,160 Z"/>
    <text class="level-code" x="36" y="78">E6</text>
    <text class="room-number" x="38" y="110">1230</text>
    <text class="room-name" x="418" y="172" text-anchor="end">WC-Damen</text>
    <text class="home-name" x="34" y="272">BIRKENAU</text>
  </svg>

</main>
</body>
</html>
```